Baby and Kids e-shop (Russian language is needed)

We need a web design for e-shop of a Russian company based in Moscow. We sell maternity things, baby and kids goods, clothes, toys, furniture, home and decor, etc.
We need the design that will suit to the exhisting logo. It should be simple and comfortable to the consumers. Attractive but not too bright (so that the goods' pictures attract more attention to them instead of the design).
The domain name of the company is quillbeck.ru
Design of the main page should be similar to the idea of lulloday.com All button names of the main page are provided in attached file.
While choosing certain category from the menu, we should see the list of goods to the left and list of brands to the right (example: http://www.krovatka-dom.ru/?welcome).

We need:
- main page
- page of the catalogue
- page of the certain category from the catalogue
- page with a certain good
- cart page
- payment page
- quill beck club page (banner and text)
- registration page (banner, registration form, text)
Updates

Target Market(s)

pregnant women, young moms

Industry/Entity Type

Baby

Requirements
Must have
• The webdesign should be very clear and similar to lulloday.com You can suggest a kind of design similar to kindrelo.de, tappelo.de.
The web design should clear state that it is targeted on kids goods, but it is a family e-shop as well.
Nice to have
• 1) In general the design shall be the same as provided sample we like. The design of a page with a concrete good should have tabs: 1) about this good, 2) payment, 3) delivery and return, 4) review; like this: http://www.harbordressco.com/t-shirts-c4/vornik-classic-h-tee-ridge-t-shirt-p81174
2) we need design of stickers like in shown example above: 5% off (First order) and Free Coupon for X Rubles for every 1000 Rubles spent online
3) instead of Bookmark&share, ask a question, e-mail a friend and add to wish list, we should have "share" (Chatterly, Druzhnet, Svoyakh - short logos, I will send examples), "ask a question", "e-mail a friend" and "add to gift list" (All this information is contained in downloaded files).

```html
<!DOCTYPE html>
<html lang="ru">
<head>
<meta charset="utf-8">
<title>quill beck — интернет магазин для детей</title>
<link rel="stylesheet" href="https://fonts.googleapis.com/css2?family=PT+Sans:ital,wght@0,400;0,700;1,400;1,700&display=swap">
<style>
:root{
  --sky:#cfe6f1;
  --paper:#ffffff;
  --ink:#3b3b3b;
  --muted:#7a7a7a;
  --red:#e2342b;
  --orange:#f28a1e;
  --green:#8cc63f;
  --green-dark:#5f9a22;
  --blue:#3ba3d9;
  --slate:#3e4a55;
  --line:#e2e2e2;
  --soft:#f4f8fb;
}
*{box-sizing:border-box;margin:0;padding:0}
html,body{width:1200px;height:2352px;overflow:hidden}
body{background:var(--sky);font-family:"PT Sans",Arial,sans-serif;color:var(--ink);font-size:12px;position:relative}
.page{position:absolute;left:72px;top:0;width:1056px;height:2290px;background:var(--paper);box-shadow:0 0 14px rgba(60,110,140,.25);border-radius:0 0 18px 18px;overflow:hidden}

/* header */
.header{position:relative;height:188px}
.brand{position:absolute;left:24px;top:14px;width:190px;display:flex;flex-direction:column;align-items:center;gap:6px}
.brand-dot{width:96px;height:96px;border-radius:50%;background:var(--orange)}
.brand-name{font-size:24px;font-weight:700;color:var(--red);line-height:26px}
.cart{position:absolute;left:230px;top:16px;width:100px;font-size:11px;color:var(--muted);line-height:15px}
.cart b{color:var(--green-dark)}
.tagline{position:absolute;left:350px;top:20px;width:260px;font-size:18px;line-height:22px;font-weight:700;font-style:italic;color:var(--red)}
.phones{position:absolute;left:640px;top:18px;width:170px;font-size:15px;font-weight:700;line-height:22px}
.login{position:absolute;right:24px;top:14px;width:190px;font-size:11px}
.login .forgot{color:var(--red);font-size:13px;font-weight:700;margin-bottom:6px}
.login input{display:block;width:100%;height:22px;border:1px solid #cfcfcf;border-radius:3px;margin-bottom:5px;font:inherit;padding:0 6px}
.login .row{display:flex;justify-content:space-between;align-items:center;margin-top:4px}
.btn{display:inline-block;background:var(--green);color:#fff;font-weight:700;border-radius:3px;padding:3px 10px}
.nav{position:absolute;left:16px;right:16px;bottom:0;height:34px;display:flex;gap:4px;align-items:flex-end}
.nav a{flex:1;height:30px;line-height:30px;text-align:center;font-size:11px;font-weight:700;color:#fff;border-radius:8px 8px 0 0;text-decoration:none}
.nav a:nth-child(1){background:#f2a93b}.nav a:nth-child(2){background:#e86b6b}
.nav a:nth-child(3){background:#9ac94b}.nav a:nth-child(4){background:#5ab4df}
.nav a:nth-child(5){background:#b48ad6}.nav a:nth-child(6){background:#f08fb3}
.nav a:nth-child(7){background:#4fc0b0}.nav a:nth-child(8){background:#f2c23b}
.navbar-line{height:6px;background:var(--green)}

/* body area */
.body{position:relative;height:790px}
.sidebar{position:absolute;left:14px;top:14px;width:200px}
.panel-head{background:var(--green);color:#fff;font-weight:700;font-size:13px;padding:6px 10px;border-radius:6px 6px 0 0}
.catalog{border:1px solid var(--line);border-top:0;list-style:none}
.catalog li{display:flex;align-items:center;gap:7px;padding:5px 8px;font-size:11px;border-bottom:1px dotted var(--line)}
.catalog li::before{content:"";width:10px;height:10px;border-radius:50%;background:var(--orange);flex:none}
.catalog li:nth-child(3n+2)::before{background:var(--blue)}
.catalog li:nth-child(3n)::before{background:var(--green)}
.side-box{margin-top:12px;border:1px solid var(--line);border-radius:6px;padding:10px;font-size:11px;line-height:15px;color:var(--muted);height:150px}
.side-box h4{color:var(--red);font-size:12px;margin-bottom:4px}

.main{position:absolute;left:228px;top:14px;width:814px}
.hero{position:relative;height:290px;border-radius:8px;background:linear-gradient(135deg,#f6dfe9,#e7f2d8 55%,#fbe9c7)}
.hero-tabs{position:absolute;right:0;top:0;display:flex;gap:4px}
.hero-tabs span{background:#fff;padding:4px 10px;border-radius:0 0 6px 6px;font-size:12px;font-weight:700;color:var(--blue)}
.news{display:flex;gap:10px;margin-top:10px}
.news-card{flex:1;border:1px solid var(--line);border-radius:6px;overflow:hidden}
.news-card .date{color:#fff;font-weight:700;font-size:11px;padding:4px 8px;background:var(--blue)}
.news-card:nth-child(n+2) .date{background:var(--red)}
.news-card .thumb{height:50px;background:#eef3f6}
.news-card p{font-size:10px;line-height:13px;color:var(--muted);padding:5px 8px}
.goods{display:flex;gap:10px;margin-top:10px}
.goods div{flex:1;height:330px;border-radius:6px}

/* product finder */
.finder{position:absolute;left:14px;top:1000px;width:694px;height:196px;background:var(--slate);border-radius:8px;padding:12px 14px;color:#fff}
.finder h3{font-size:14px;margin-bottom:10px}
.finder .rows{display:flex;gap:14px}
.finder .fields{width:250px}
.finder .field{display:flex;justify-content:space-between;align-items:center;font-size:11px;margin-bottom:8px}
.finder .field span:last-child{width:120px;height:20px;background:#fff;border-radius:3px;color:var(--muted);padding:2px 6px;font-size:10px}
.finder .picks{flex:1;display:grid;grid-template-columns:repeat(3,1fr);gap:8px}
.finder .picks div{background:#fff;border-radius:4px;color:var(--slate);font-weight:700;font-size:13px;display:flex;align-items:center;justify-content:center}
.promo{position:absolute;left:722px;top:1000px;width:320px;height:196px;border-radius:8px;background:linear-gradient(160deg,#3aa0d8,#7cc8ee)}

/* brands */
.brands{position:absolute;left:14px;top:1212px;width:1028px;display:grid;grid-template-columns:repeat(9,1fr);gap:8px}
.brands span{height:52px;display:flex;align-items:center;justify-content:center;font-weight:700;font-size:15px;border:1px solid var(--line);border-radius:6px}
.brands span:nth-child(4n+1){color:var(--red)}.brands span:nth-child(4n+2){color:var(--blue)}
.brands span:nth-child(4n+3){color:var(--green-dark)}.brands span:nth-child(4n){color:var(--orange)}

/* welcome */
.welcome{position:absolute;left:60px;top:1360px;width:936px;font-size:12.5px;line-height:19px;color:var(--ink)}
.welcome h1{text-align:center;font-size:18px;color:var(--red);margin-bottom:16px}
.welcome p{margin-bottom:12px}
.welcome ul{margin:0 0 12px 18px}
.welcome a{color:var(--blue)}

/* footer */
.footer{position:absolute;left:0;top:1900px;width:1056px;height:390px;background:var(--soft)}
.footer svg{position:absolute;top:-1px;left:0}
.foot-cols{position:absolute;top:60px;left:30px;right:30px;display:flex;gap:30px;font-size:11px;line-height:17px;color:var(--muted)}
.foot-cols b{color:var(--ink)}
.pay{display:flex;gap:8px;margin-top:8px}
.pay i{width:40px;height:24px;border-radius:4px;background:#dbe4ea}
.social{display:flex;gap:10px;margin-top:8px;color:var(--blue);font-weight:700}
.popular{position:absolute;left:30px;right:30px;top:250px;text-align:center;font-size:11px;line-height:17px;color:var(--muted)}
.popular b{font-size:13px;color:var(--red)}
.copy{position:absolute;left:30px;right:30px;top:340px;text-align:center;font-size:10px;color:var(--muted)}
</style>
</head>
<body>
<div class="page">
  <header class="header">
    <div class="brand"><span class="brand-dot"></span><span class="brand-name">quill beck</span></div>
    <div class="cart"><b>КОРЗИНА</b><br>товаров: 0<br>сумма: 0 руб.</div>
    <div class="tagline">Интернет магазин для детей</div>
    <div class="phones">+7 (495) 000-12-34<br>+7 (495) 000-56-78</div>
    <form class="login">
      <div class="forgot">Забыли пароль?</div>
      <input placeholder="Логин">
      <input placeholder="Пароль">
      <div class="row"><span>Запомнить</span><span class="btn">Войти</span></div>
    </form>
    <nav class="nav">
      <a>О МАГАЗИНЕ</a><a>ОПЛАТА И ДОСТАВКА</a><a>НОВОСТИ</a><a>ПОДАРКИ</a>
      <a>КЛУБ QUILL BECK</a><a>ОТЗЫВЫ</a><a>АКЦИИ</a><a>КОНТАКТЫ</a>
    </nav>
  </header>
  <div class="navbar-line"></div>

  <section class="body">
    <aside class="sidebar">
      <div class="panel-head">КАТАЛОГ</div>
      <ul class="catalog">
        <li>Для будущих мам</li><li>Детское питание</li><li>Гигиена и уход</li>
        <li>Кормление</li><li>Одежда</li><li>Обувь</li><li>Игрушки</li>
        <li>Коляски</li><li>Автокресла</li><li>Детская мебель</li><li>Текстиль</li>
        <li>Прогулки и путешествия</li><li>Развитие и творчество</li><li>Книги</li>
        <li>Спорт и отдых</li><li>Купание</li><li>Безопасность</li>
        <li>Дом и декор</li><li>Подарки</li><li>Для всей семьи</li>
      </ul>
      <div class="side-box">
        <h4>Клуб quill beck</h4>
        Скидки и подарки для постоянных покупателей нашего магазина. Вступайте в клуб и получайте бонусы с каждой покупки.
      </div>
    </aside>

    <div class="main">
      <div class="hero" role="img" aria-label="Баннер с мягкими игрушками">
        <div class="hero-tabs"><span>Авторизация</span><span>Регистрация</span></div>
      </div>
      <div class="news">
        <div class="news-card"><div class="date">01.11.2013 Новые поступления</div><div class="thumb" role="img" aria-label="Фото новинки"></div><p>Новая коллекция зимней одежды уже в каталоге магазина.</p></div>
        <div class="news-card"><div class="date">28.10.2013 Праздник недели</div><div class="thumb" role="img" aria-label="Фото праздника"></div><p>Скидки на игрушки и товары для творчества всю неделю.</p></div>
        <div class="news-card"><div class="date">18.10.2013 Удобная доставка</div><div class="thumb" role="img" aria-label="Фото доставки"></div><p>Бесплатная доставка по Москве при заказе от 3000 руб.</p></div>
      </div>
      <div class="goods">
        <div role="img" aria-label="Фото игрушки" style="background:#f7d9c4"></div>
        <div role="img" aria-label="Фото детской одежды" style="background:#d7ecc4"></div>
        <div role="img" aria-label="Фото коляски" style="background:#cfe3f3"></div>
        <div role="img" aria-label="Фото товаров для мам" style="background:#f3d3e2"></div>
      </div>
    </div>
  </section>

  <section class="finder">
    <h3>ПОДБОР ТОВАРА</h3>
    <div class="rows">
      <div class="fields">
        <div class="field"><span>Детские игрушки</span><span>Все бренды</span></div>
        <div class="field"><span>Детская одежда</span><span>Все бренды</span></div>
        <div class="field"><span>Детское питание</span><span>Все бренды</span></div>
        <div class="field"><span>Коляски</span><span>Все бренды</span></div>
        <div class="field"><span>Для мам</span><span>Все бренды</span></div>
      </div>
      <div class="picks">
        <div>Mirla</div><div>Kokoro</div><div>Dorfel</div>
        <div>Nivo</div><div>Pelli</div><div>Solvika</div>
      </div>
    </div>
  </section>
  <div class="promo" role="img" aria-label="Рекламный баннер с детскими героями"></div>

  <section class="brands">
    <span>Lantiko</span><span>Bembi</span><span>Vesna</span><span>Ilka</span><span>Pelli</span><span>Kastrel</span><span>Nivo</span><span>Mirla</span><span>Dorfel</span>
    <span>Solvika</span><span>Kokoro</span><span>Tusya</span><span>Ralin</span><span>Gemmi</span><span>Orsa</span><span>Brinka</span><span>Luvio</span><span>Semik</span>
  </section>

  <section class="welcome">
    <h1>Добро пожаловать в интернет магазин для детей Quill Beck!</h1>
    <p>Мы понимаем, что для того, чтобы ваш ребенок вырос здоровым, умным и счастливым, ему необходимо уделять много времени. Поэтому мы собрали в одном месте всё, что может понадобиться малышу и его родителям: от одежды и игрушек до мебели и товаров для дома. Покупки в нашем интернет магазине экономят ваше время и силы.</p>
    <ul>
      <li>одежда для новорожденных, малышей и школьников;</li>
      <li>игрушки, развивающие игры и товары для творчества;</li>
      <li>коляски, автокресла, кроватки и детская мебель;</li>
      <li>товары для будущих и кормящих мам.</li>
    </ul>
    <p>В нашем интернет магазине товаров для детей вы найдете продукцию проверенных производителей. Мы тщательно выбираем каждый товар, следим за его качеством и безопасностью, а наши консультанты всегда готовы помочь с выбором и ответить на вопросы.</p>
    <p>Мы ценим каждого покупателя, поэтому для участников <a>клуба quill beck</a> действуют постоянные скидки, бонусы и подарки. Зарегистрируйтесь на сайте, чтобы первыми узнавать о новинках и специальных предложениях.</p>
    <p>Доставка по Москве осуществляется в удобное для вас время, а в регионы мы отправляем заказы надежными транспортными компаниями. Оплатить покупку можно наличными, банковской картой или электронными деньгами.</p>
    <p>Для будущих мам у нас есть отдельный раздел с одеждой, косметикой и полезными мелочами. Мы регулярно обновляем ассортимент и следим за тем, чтобы цены оставались доступными для каждой семьи.</p>
    <p>Желаем вам приятных покупок в интернет магазине quillbeck.ru!</p>
  </section>

  <footer class="footer">
    <svg width="1056" height="40" viewBox="0 0 1056 40" aria-hidden="true"><path d="M0 0H1056V18C960 38 880 2 790 18S620 38 528 18 350 2 260 18 90 38 0 18Z" fill="#ffffff"/></svg>
    <div class="foot-cols">
      <div><b>+7 (495) 000-12-34</b><br>Заказы принимаются 9:00 — 21:00<br>info@quillbeck.ru
        <div class="pay"><i></i><i></i><i></i><i></i></div></div>
      <div><b>Покупателям</b><br>Оплата и доставка<br>Обмен и возврат<br>Клуб quill beck</div>
      <div><b>О магазине</b><br>Новости<br>Отзывы<br>Контакты</div>
      <div><b>Мы в сетях</b><div class="social"><span>Chatterly</span><span>Druzhnet</span><span>Svoyakh</span></div></div>
    </div>
    <div class="popular"><b>Популярные разделы:</b> детская одежда, игрушки, коляски, автокресла, детская мебель, товары для мам, кормление, гигиена и уход, развитие и творчество, подарки, книги, спорт и отдых, дом и декор</div>
    <div class="copy">© 2013 quillbeck.ru — интернет магазин для детей. Все права защищены.</div>
  </footer>
</div>
</body>
</html>
```